Popup Nightclub Grand Opening Flyer

We need to design a flyer for the grand opening of an upscale, exclusive nightclub called "Lanternfall". The design needs to be chic and exclusive. The background should be black and the text should primarily be white. We like minimalist designs.

Here is the text for the flyer
-
Velvetrope Atlanta Presents

Lanternfall (LOGO)

A Popup Nightclub Experience
For one night Only

Friday, October 18, 2013
Party begins at 9PM

INVITE ONLY

See invitation for location details
(Velvetrope Atlanta logo)

-
Examples we like

http://cdn2-b.brivelpost.com/sites/default/files/styles/image_content_width/hash/3d/fa/1472093815_4471_flyer.jpg?itok=R8kqWm2z

http://api.plovra.com/files/7Kqq-Tr82XXB3pQzJvmtR5HL2W719E4nbRtC6KLd4HsfM8Y2qTDK-VmjwDoNqLX4QBzTHD9nakRbVx3m-Pfq8htc3MDTWr5p4/2zelSaturdays.jpg

http://quenmar.com/wp-content/uploads/yootheme/widgetkit/gallery/2zel/2zel-gen_vroom4-01.jpg

Hi All, one thing that we are seeing that we don't like is on over emphasis on the phrase "a popup nightclub experience" please don't make this the largest thing on the flyer

Target Market(s)

Target market is 25-35 year olds who are affluent (rich) and like luxury brands

Requirements
Must have
• Dark Background
Nice to have
• Velvetrope Logo on the bottom
Modern text that isn't curvy
Should not have
• Curved text

```html
<!DOCTYPE html>
<html lang="en">
<head>
<meta charset="utf-8">
<title>Lanternfall – A Popup Nightclub Experience</title>
<link href="https://fonts.googleapis.com/css2?family=Nunito:wght@700;800&family=Open+Sans:wght@300;400&family=Roboto+Condensed:wght@700&display=swap" rel="stylesheet">
<style>
  :root {
    --ink: #000000;
    --white: #ffffff;
    --silver: #c9d2d6;
    --silver-dark: #5f6a70;
    --mint: #9fe6df;
    --violet: #5a2f6e;
    --gold: #f2e6a6;
    --headline: #d6d6d6;
  }
  * { margin: 0; padding: 0; box-sizing: border-box; }
  html, body {
    width: 1200px; height: 703px; overflow: hidden; background: var(--ink);
  }
  .flyer {
    position: relative; width: 1200px; height: 703px; overflow: hidden;
    background:
      linear-gradient(62deg, transparent 43%, rgba(90,47,110,0.55) 50%, transparent 57%),
      radial-gradient(ellipse 420px 260px at 600px 360px, rgba(70,40,90,0.35), transparent 70%),
      var(--ink);
    color: var(--white);
    font-family: "Nunito", "Open Sans", sans-serif;
  }
  .presenter {
    position: absolute; top: 34px; left: 0; width: 100%;
    text-align: center; font-size: 22px; font-weight: 800; line-height: 28px;
  }
  .frame {
    position: absolute; left: 150px; top: 145px; width: 900px; height: 415px;
    border-radius: 40px 40px 120px 120px;
    background:
      radial-gradient(ellipse at 50% 0%, rgba(159,230,223,0.45), transparent 45%),
      linear-gradient(180deg, var(--silver) 0%, var(--silver-dark) 55%, var(--silver) 100%);
    opacity: 0.85;
  }
  .frame-panel {
    position: absolute; left: 220px; top: 200px; width: 760px; height: 240px;
    border-radius: 18px;
    background: radial-gradient(ellipse at 50% 40%, #1c1c1c, #050505 80%);
  }
  .venue {
    position: absolute; top: 262px; left: 0; width: 100%; text-align: center;
    font-family: "Open Sans", sans-serif; font-weight: 300;
  }
  .venue-name {
    display: block; font-size: 44px; line-height: 52px; font-weight: 300; letter-spacing: 8px; color: var(--white);
  }
  .venue-type {
    display: block; font-size: 12px; line-height: 16px; font-weight: 400; letter-spacing: 4px; color: var(--silver);
  }
  .headline {
    position: absolute; top: 340px; left: 0; width: 100%; text-align: center;
    font-size: 32px; line-height: 40px; font-weight: 800; letter-spacing: -0.5px; color: var(--headline);
  }
  .tagline {
    position: absolute; top: 398px; left: 0; width: 100%; text-align: center;
    font-family: "Open Sans", sans-serif; font-size: 16px; line-height: 22px; letter-spacing: 4px; color: var(--gold);
  }
  .when {
    position: absolute; left: 80px; top: 577px; width: 400px; text-align: center;
    font-size: 21px; font-weight: 800; line-height: 28px; letter-spacing: 0.5px;
  }
  .rule { position: absolute; top: 640px; height: 1px; background: var(--silver); }
  .rule-left { left: 80px; width: 396px; }
  .rule-right { left: 725px; width: 396px; }
  .access {
    position: absolute; top: 628px; left: 480px; width: 240px; text-align: center;
    font-family: "Roboto Condensed", sans-serif; font-size: 23px; line-height: 28px; font-weight: 700; letter-spacing: -1px;
  }
  .host-mark {
    position: absolute; left: 788px; top: 545px; width: 320px;
    display: flex; align-items: center; gap: 14px;
    font-size: 28px; line-height: 36px; font-weight: 800; letter-spacing: 1px; color: var(--white);
  }
  .host-mark-dot { width: 34px; height: 34px; border-radius: 50%; background: var(--white); flex: none; }
  .location-note {
    position: absolute; left: 725px; top: 603px; width: 396px; text-align: center;
    font-family: "Roboto Condensed", sans-serif; font-size: 21px; line-height: 26px; font-weight: 700; letter-spacing: -0.8px;
  }
</style>
</head>
<body>
  <main class="flyer">
    <p class="presenter">Velvetrope Atlanta Presents</p>

    <div class="frame" role="img" aria-label="Ornate silver scroll frame around the club title"></div>
    <div class="frame-panel"></div>

    <h1 class="venue">
      <span class="venue-name">LANTERNFALL</span>
      <span class="venue-type">NIGHTCLUB</span>
    </h1>
    <h2 class="headline">A Popup Nightclub Experience</h2>
    <p class="tagline">For One Night Only</p>

    <p class="when">Friday, October 18, 2013<br>Party Begins at 9PM</p>
    <div class="rule rule-left"></div>

    <p class="access">INVITE ONLY</p>

    <div class="host-mark"><span class="host-mark-dot"></span><span>VELVETROPE</span></div>
    <p class="location-note">See invitation for location details.</p>
    <div class="rule rule-right"></div>
  </main>
</body>
</html>
```